Financial Planning Firm needs a client data collection summary sheet to print on A3

We are a financial advice company, and we are after a 1-page sheet where we can write all of the client’s personal information in our meetings, like a mind map.
It should have our logo on the page along with a place to put the Client's Name and the Date.
It also needs to have the following Headings
Family
Home
Investments
Business
Estate Plan
Lifestyle
Money
Retirement
Dreams & Goals
Health and Wellbeing
It also needs to have our License details on the bottom: Bellwood Counsel Pty Ltd (839162) is an Authorised Representative of Corrin Heritage Capital Group Pty Ltd AFSL No: 617058 ABN 72 915 483 206. This document has been prepared by Bellwood Counsel and is for general information only.
Please utilise our colour scheme as per our logo attached. Please find uploaded to the project an example data collection summary sheet that we use currently.

```html
<!DOCTYPE html>
<html lang="en">
<head>
<meta charset="utf-8">
<title>Bellwood Counsel – Personal Information Form</title>
<link href="https://fonts.googleapis.com/css2?family=Fira+Sans+Condensed:ital,wght@0,400;0,700;1,600&display=swap" rel="stylesheet">
<style>
  :root{
    --bg:#ececec;
    --paper:#ffffff;
    --ink:#111111;
    --gold:#c9a272;
    --gold-light:#e2c49c;
    --rule:#222222;
    --muted:#555555;
  }
  *{box-sizing:border-box;margin:0;padding:0}
  html,body{width:1200px;height:784px;overflow:hidden;background:var(--bg)}
  .sheet{
    position:absolute;left:338px;top:22px;width:524px;height:740px;
    background:var(--paper);box-shadow:0 2px 10px rgba(0,0,0,.12);
    font-family:"Fira Sans Condensed",sans-serif;color:var(--ink);overflow:hidden;
  }
  .corner{position:absolute;width:60px;height:8px;background:linear-gradient(90deg,var(--gold),var(--gold-light))}
  .corner--tl{left:0;top:0;clip-path:polygon(0 0,100% 0,85% 100%,0 100%)}
  .corner--tr{right:0;top:0;clip-path:polygon(0 0,100% 0,100% 100%,15% 100%)}
  .corner--bl{left:0;bottom:0;clip-path:polygon(0 0,85% 0,100% 100%,0 100%)}
  .corner--br{right:0;bottom:0;clip-path:polygon(15% 0,100% 0,100% 100%,0 100%)}

  .brand{position:absolute;left:0;right:0;top:28px;text-align:center}
  .brand__name{font-family:"Fira Sans Condensed",sans-serif;font-weight:700;font-size:26px;line-height:1;color:var(--ink);display:inline-flex;align-items:center;gap:8px}
  .brand__mark{width:12px;height:12px;background:var(--ink);display:inline-block}
  .brand__tagline{font-size:10px;letter-spacing:1px;margin-top:8px;color:var(--ink)}
  .brand__form{font-size:8px;font-weight:700;letter-spacing:1px;margin-top:3px;color:var(--muted)}
  .brand__band{position:absolute;top:20px;height:12px;width:70px}
  .brand__band--left{left:0;background:linear-gradient(90deg,#000,#888)}
  .brand__band--right{right:0;background:linear-gradient(90deg,#888,#000)}

  .field-name{position:absolute;left:30px;top:104px;display:flex;align-items:center;gap:6px;font-size:8px}
  .field-name__box{width:300px;height:12px;border:1px solid var(--muted)}
  .field-date{position:absolute;right:30px;top:104px;display:flex;align-items:center;gap:3px;font-size:8px}
  .field-date span{margin-right:3px}
  .field-date i{width:12px;height:12px;border:1px solid var(--muted);display:block}

  .topics{position:absolute;left:30px;right:30px;top:140px;display:grid;grid-template-columns:repeat(3,1fr);column-gap:14px}
  .topics__col{display:flex;flex-direction:column;gap:10px}
  .topic{display:flex;align-items:center;gap:6px}
  .topic__bar{flex:1;height:16px;padding-left:6px;display:flex;align-items:center;
    background:linear-gradient(90deg,#1a1a1a 0%,#6a6a6a 45%,#2a2a2a 80%,#000 100%);
    color:#fff;font-style:italic;font-weight:600;font-size:9.5px;position:relative}
  .topic__bar::after{content:"";position:absolute;left:0;right:0;bottom:-2px;height:1px;background:var(--gold)}
  .topic__check{width:13px;height:13px;border:1px solid var(--muted)}

  .remarks{position:absolute;left:30px;right:30px;top:268px}
  .remarks__label{font-weight:700;font-size:11px}
  .remarks__lines{margin-top:6px;display:flex;flex-direction:column}
  .remarks__lines li{list-style:none;height:23px;border-bottom:1px solid var(--rule)}

  .footer__band{position:absolute;left:60px;right:60px;bottom:50px;height:1px;background:linear-gradient(90deg,transparent,#000 20%,#000 80%,transparent)}
  .footer{position:absolute;left:0;right:0;bottom:14px;text-align:center}
  .footer__name{font-weight:700;font-size:8px;line-height:1}
  .footer__legal{font-size:5.6px;line-height:1.35;color:var(--ink);margin-top:5px;padding:0 24px}
</style>
</head>
<body>
<main class="sheet">
  <span class="corner corner--tl"></span><span class="corner corner--tr"></span>
  <span class="corner corner--bl"></span><span class="corner corner--br"></span>

  <header class="brand">
    <span class="brand__band brand__band--left"></span>
    <span class="brand__band brand__band--right"></span>
    <div class="brand__name"><span class="brand__mark"></span>Bellwood Counsel</div>
    <div class="brand__tagline">Your Financial Expert</div>
    <div class="brand__form">PERSONAL INFORMATION FORM</div>
  </header>

  <div class="field-name"><span>Name</span><span class="field-name__box"></span></div>
  <div class="field-date"><span>SOC Date</span><i></i><i></i><i></i><i></i><i></i><i></i></div>

  <section class="topics">
    <div class="topics__col">
      <div class="topic"><span class="topic__bar">Family</span><span class="topic__check"></span></div>
      <div class="topic"><span class="topic__bar">Business</span><span class="topic__check"></span></div>
      <div class="topic"><span class="topic__bar">Money</span><span class="topic__check"></span></div>
      <div class="topic"><span class="topic__bar">Health and Wellbeing</span><span class="topic__check"></span></div>
    </div>
    <div class="topics__col">
      <div class="topic"><span class="topic__bar">Home</span><span class="topic__check"></span></div>
      <div class="topic"><span class="topic__bar">Estate Plan</span><span class="topic__check"></span></div>
      <div class="topic"><span class="topic__bar">Retirement</span><span class="topic__check"></span></div>
    </div>
    <div class="topics__col">
      <div class="topic"><span class="topic__bar">Investments</span><span class="topic__check"></span></div>
      <div class="topic"><span class="topic__bar">Lifestyle</span><span class="topic__check"></span></div>
      <div class="topic"><span class="topic__bar">Dreams &amp; Goals</span><span class="topic__check"></span></div>
    </div>
  </section>

  <section class="remarks">
    <div class="remarks__label">REMARKS:</div>
    <ul class="remarks__lines">
      <li></li><li></li><li></li><li></li><li></li><li></li><li></li><li></li>
      <li></li><li></li><li></li><li></li><li></li><li></li><li></li><li></li><li></li>
    </ul>
  </section>

  <span class="footer__band"></span>
  <footer class="footer">
    <div class="footer__name">Bellwood Counsel Pty Ltd</div>
    <p class="footer__legal">Bellwood Counsel Pty Ltd (839162) is an Authorised Representative of Corrin Heritage Capital Group Pty Ltd AFSL No: 617058 ABN 72 915 483 206. This document has been prepared by Bellwood Counsel and is for general information only.</p>
  </footer>
</main>
</body>
</html>
```